Business card design needed

I need a business card design for a dog walking, dog minding and dog training business. Please refer to my website for the basic company colours and fonts I'm after. Planning on a double sided card, so all information doesn't need to be on the 'front' side.
Cheers

Industry/Entity Type

Dog Training

Contact Information for Business Card

Bramble Paws - guiding hounds
Ned 0487306914
bramblepawsdemo.com.au
-walking
-holiday stays
-onsite care
-training and behavioural consultations

```html
<!DOCTYPE html>
<html lang="en">
<head>
<meta charset="utf-8">
<title>Bramble Paws – business card</title>
<link href="https://fonts.googleapis.com/css2?family=Fira+Sans:wght@400;500&display=swap" rel="stylesheet">
<style>
  :root {
    --page: #ffffff;
    --card: #ffffff;
    --brand-orange: #e2451e;
    --ink: #2a2a2a;
    --silhouette-a: #c9c9ca;
    --silhouette-b: #e2e2e3;
    --shadow: rgba(0, 0, 0, 0.35);
  }
  html, body {
    margin: 0;
    padding: 0;
    width: 848px;
    height: 1200px;
    overflow: hidden;
    background: var(--page);
    font-family: "Fira Sans", Arial, sans-serif;
  }
  .canvas {
    position: relative;
    width: 848px;
    height: 1200px;
  }
  .card {
    position: absolute;
    left: 135px;
    width: 582px;
    height: 328px;
    background: var(--card);
    box-shadow: 5px 6px 7px var(--shadow);
    overflow: hidden;
  }
  .card--front { top: 215px; }
  .card--back { top: 657px; }

  .dog-artwork {
    position: absolute;
    left: 135px;
    top: 20px;
    width: 385px;
    height: 308px;
    border-radius: 40px 40px 0 0;
    background: linear-gradient(100deg, var(--silhouette-a) 0%, var(--silhouette-a) 50%, var(--silhouette-b) 52%, var(--silhouette-b) 100%);
    opacity: 0.55;
  }

  .brand-name {
    position: absolute;
    left: 27px;
    top: 20px;
    margin: 0;
    font-size: 38px;
    font-weight: 500;
    letter-spacing: 0.5px;
    line-height: 1;
    color: var(--brand-orange);
    text-transform: uppercase;
  }
  .tagline {
    position: absolute;
    left: 405px;
    top: 48px;
    margin: 0;
    font-size: 15px;
    font-weight: 400;
    color: var(--ink);
  }

  .contact-band {
    position: absolute;
    left: 0;
    top: 245px;
    width: 582px;
    height: 38px;
    background: var(--brand-orange);
    color: #ffffff;
    font-size: 24px;
    line-height: 38px;
  }
  .contact-band .website {
    position: absolute;
    left: 27px;
  }
  .contact-band .phone {
    position: absolute;
    right: 32px;
  }

  .services {
    position: absolute;
    left: 0;
    top: 126px;
    width: 582px;
    margin: 0;
    padding: 0;
    list-style: none;
    text-align: center;
    color: var(--brand-orange);
    font-size: 24px;
    font-weight: 500;
    line-height: 43px;
  }
  .services li::before,
  .services li::after {
    content: "";
    display: inline-block;
    width: 6px;
    height: 6px;
    background: var(--brand-orange);
    vertical-align: middle;
    margin: 0 8px;
  }
</style>
</head>
<body>
<div class="canvas">

  <section class="card card--front">
    <div class="dog-artwork" role="img" aria-label="Grey silhouettes of two standing dogs"></div>
    <h1 class="brand-name">Bramble Paws</h1>
    <p class="tagline">guiding hounds</p>
    <div class="contact-band">
      <span class="website">bramblepawsdemo.com.au</span>
      <span class="phone">Ned 048 730 69 14</span>
    </div>
  </section>

  <section class="card card--back">
    <div class="dog-artwork" role="img" aria-label="Grey silhouettes of two standing dogs"></div>
    <h2 class="brand-name">Bramble Paws</h2>
    <p class="tagline">guiding hounds</p>
    <ul class="services">
      <li>walking</li>
      <li>holiday stays</li>
      <li>onsite care</li>
      <li>training and behavioural consultations</li>
    </ul>
  </section>

</div>
</body>
</html>
```